Criação de Papelaria (6 itens) para Marketing & Comunicação
" Entregamos os projetos sempre com criatividade e tentando transmitir ao máximo emoção ao consumidor. "

```html
<!DOCTYPE html>
<html lang="pt-BR">
<head>
<meta charset="utf-8">
<title>Lumen Propaganda – Cartão de Visita</title>
<link rel="stylesheet" href="https://fonts.googleapis.com/css2?family=Roboto+Condensed:wght@400;700&display=swap">
<style>
  :root {
    --bg: #2b2a29;
    --orange: #f1a234;
    --white: #ffffff;
    --charcoal: #3f3f41;
    --icon-box: #3a3a3c;
  }
  * { margin: 0; padding: 0; box-sizing: border-box; }
  html, body { width: 1200px; height: 1200px; overflow: hidden; }
  body {
    background: var(--bg);
    font-family: "Roboto Condensed", "Arial Narrow", sans-serif;
    display: flex; align-items: center; justify-content: center;
  }
  .business-card {
    position: relative;
    width: 1000px; height: 556px;
    background: var(--orange);
    overflow: hidden;
    color: var(--white);
  }
  .brand {
    position: absolute; left: 58px; top: 150px; width: 300px;
    font-weight: 400; color: var(--white); text-transform: uppercase;
  }
  .brand-name { font-size: 78px; letter-spacing: 14px; line-height: 1; }
  .brand-sub { font-size: 25px; letter-spacing: 11px; margin-top: 8px; line-height: 1; }
  .contact {
    position: absolute; left: 432px; top: 40px; right: 40px;
    text-transform: uppercase;
  }
  .person-name { font-weight: 700; font-size: 27px; letter-spacing: 0.5px; }
  .person-role { font-weight: 400; font-size: 25px; margin-top: 2px; }
  .contact-row {
    position: absolute; left: 0; display: flex; align-items: flex-start; gap: 20px;
    font-size: 27px; line-height: 32px;
  }
  .row-phone { top: 110px; }
  .row-address { top: 165px; }
  .row-web { top: 253px; }
  .icon {
    width: 32px; height: 32px; flex: none; border-radius: 4px;
    background: var(--icon-box); display: flex; align-items: center; justify-content: center;
  }
  .waves { position: absolute; left: 0; bottom: 0; width: 1000px; height: 556px; }
</style>
</head>
<body>
  <div class="business-card">
    <div class="brand">
      <div class="brand-name">Lumen</div>
      <div class="brand-sub">Propaganda</div>
    </div>

    <div class="contact">
      <div class="person-name">Nome Completo da Silva</div>
      <div class="person-role">Cargo | Função</div>

      <div class="contact-row row-phone">
        <span class="icon">
          <svg width="20" height="20" viewBox="0 0 20 20"><rect x="5" y="2" width="10" height="16" rx="1.5" fill="none" stroke="#fff" stroke-width="1.6"/><line x1="8.5" y1="15.5" x2="11.5" y2="15.5" stroke="#fff" stroke-width="1.4"/></svg>
        </span>
        <span>99 9 9999 9999 | 9 9999 9999</span>
      </div>

      <div class="contact-row row-address">
        <span class="icon">
          <svg width="20" height="20" viewBox="0 0 20 20"><path d="M10 18 C5 12 4 10 4 8 A6 6 0 0 1 16 8 C16 10 15 12 10 18 Z" fill="none" stroke="#fff" stroke-width="1.6"/><circle cx="10" cy="8" r="2.2" fill="#fff"/></svg>
        </span>
        <span>Rua da Luz, 123 - Centro<br>Cidade - UF | 99.000-000</span>
      </div>

      <div class="contact-row row-web">
        <span class="icon">
          <svg width="20" height="20" viewBox="0 0 20 20"><circle cx="10" cy="10" r="7" fill="none" stroke="#fff" stroke-width="1.5"/><ellipse cx="10" cy="10" rx="3" ry="7" fill="none" stroke="#fff" stroke-width="1.2"/><line x1="3" y1="10" x2="17" y2="10" stroke="#fff" stroke-width="1.2"/></svg>
        </span>
        <span>www.lumenprop.com.br</span>
      </div>
    </div>

    <svg class="waves" viewBox="0 0 1000 556" aria-hidden="true">
      <path fill="var(--white)" d="M0,405 C20,382 40,375 62.5,375 S105,382 125,405 S165,435 187.5,435 S230,428 250,405 S290,375 312.5,375 S355,382 375,405 S415,435 437.5,435 S480,428 500,405 S540,375 562.5,375 S605,382 625,405 S665,435 687.5,435 S730,428 750,405 S790,375 812.5,375 S855,382 875,405 S915,435 937.5,435 S980,428 1000,405 L1000,556 L0,556 Z"/>
      <path fill="var(--charcoal)" d="M0,440 C20,417 40,410 62.5,410 S105,417 125,440 S165,470 187.5,470 S230,463 250,440 S290,410 312.5,410 S355,417 375,440 S415,470 437.5,470 S480,463 500,440 S540,410 562.5,410 S605,417 625,440 S665,470 687.5,470 S730,463 750,440 S790,410 812.5,410 S855,417 875,440 S915,470 937.5,470 S980,463 1000,440 L1000,556 L0,556 Z"/>
    </svg>
  </div>
</body>
</html>
```